Dog Snacks brand needs a new packaging design

Dear Designers,

We are looking for a packaging expert to design our new line of Dog Snacks which contain a relaxing hemp extract (CBD).

Our company is already selling various relaxing cat & dog products , and we would like this new design to reflect the same "style & feeling" as our current products (see attached instructions).

Technical aspects:
- The packaging is a Stand Up Pouch (12x18.5x7cm - see attached instructions).
- Please follow technical guidelines from printer (see attached instructions).
- The packaging will contain 120g of high-quality, semi-moist dog snacks.
- We will be designing 3 differents variations for 3 different flavours: Chicken, Beef & Liver.
- The packaging will be printed with a matt finish.

Design aspects:
- The design should be compatible with our brand identity (i.e. fluffly, pure, relaxing, positive, clean & natural).
- Soft/rounded shapes are preferred.
- Please use our brand's colors (#3BA384, White & Black).
- Please use our company logo (see attached instructions).
- The design also needs to convey a strong sense of professionalism as we are an animal "healthcare" brand.
- If you want to include a dog picture, we would prefer you to use a picture of our official brand ambassador (see attached instructions).
- We have attached a number of packaging examples which we like a lot. (see attached instructions). Please only use those as general inspiration.
- Only original work (no plagiarism will be accepted).

Please don't hesitate to send us a message if you have any questions about the brand, the product or the design requirements.

We look forward to seeing your designs & working on this together !

Thanks & regards,
Marcus

Target Market(s)

Dog owners

Industry/Entity Type

Pet Care

Font styles to use
Sans Serif

Requirements
Must have
• Please see project description.
Nice to have
Should not have

```html
<!DOCTYPE html>
<html lang="en">
<head>
<meta charset="utf-8">
<title>Verdanel CBD Treats – Chicken Pouch</title>
<link rel="stylesheet" href="https://fonts.googleapis.com/css2?family=Oswald:wght@400;500&family=Montserrat:wght@500;700;800&family=Noto+Serif:wght@400&family=Cormorant+Garamond:wght@500&display=swap">
<style>
  :root {
    --brand-green: #5f9d85;
    --brand-green-deep: #3f8a6d;
    --ink: #1f231f;
    --pouch-white: #efefef;
    --stage: #f4f4f4;
    --paw-grey: #cfcfd1;
    --white: #ffffff;
  }
  * { margin: 0; padding: 0; box-sizing: border-box; }
  html, body { width: 1200px; height: 1078px; overflow: hidden; background: var(--stage); }
  .canvas { position: relative; width: 1200px; height: 1078px; overflow: hidden; }
  .pouch-art { position: absolute; left: 0; top: 0; }
  .label { position: absolute; white-space: nowrap; line-height: 1; }

  .brand-name { left: 332px; width: 515px; top: 250px; text-align: center;
    font-family: 'Noto Serif', serif; font-size: 27px; color: var(--ink); letter-spacing: 1px; }
  .brand-sub { left: 594px; top: 281px; font-family: 'Noto Serif', serif; font-size: 11px; color: var(--brand-green-deep); }

  .line-name { left: 420px; top: 516px; font-family: 'Oswald', sans-serif; font-weight: 500;
    font-size: 25px; color: var(--white); letter-spacing: 0.5px; }
  .line-name sup { font-size: 10px; vertical-align: 12px; }

  .product-cbd { left: 382px; top: 560px; font-family: 'Montserrat', sans-serif; font-weight: 700;
    font-size: 112px; letter-spacing: -2px; color: var(--white);
    -webkit-text-stroke: 2px var(--ink); text-shadow: -4px 2px 0 var(--ink); }
  .product-treats { left: 424px; top: 672px; font-family: 'Montserrat', sans-serif; font-weight: 800;
    font-size: 40px; color: var(--ink); }
  .dose { left: 447px; top: 724px; font-family: 'Montserrat', sans-serif; font-weight: 500;
    font-size: 16px; color: var(--ink); }
  .benefits { left: 637px; top: 668px; width: 168px; font-family: 'Oswald', sans-serif; font-weight: 500;
    font-size: 17px; color: var(--white); letter-spacing: 0.3px; }

  .thc-level { left: 584px; top: 807px; font-family: 'Oswald', sans-serif; font-weight: 500;
    font-size: 17px; color: var(--ink); }
  .flavor { left: 680px; top: 808px; width: 110px; text-align: center;
    font-family: 'Cormorant Garamond', serif; font-weight: 500; color: var(--ink); }
  .flavor .flavor-main { display: block; font-size: 30px; }
  .flavor .flavor-sub { display: block; font-size: 25px; margin-top: 2px; }
  .net-weight { left: 552px; top: 876px; font-family: 'Oswald', sans-serif; font-weight: 500;
    font-size: 20px; color: var(--ink); }
</style>
</head>
<body>
<div class="canvas">
  <svg class="pouch-art" width="1200" height="1078" viewBox="0 0 1200 1078">
    <defs>
      <clipPath id="pouch-clip"><rect x="332" y="133" width="515" height="832" rx="4"/></clipPath>
      <linearGradient id="photo-tone" x1="0" y1="0" x2="1" y2="1">
        <stop offset="0" stop-color="#e9e9e9"/>
        <stop offset="0.5" stop-color="#d9d6d3"/>
        <stop offset="1" stop-color="#c9c6c2"/>
      </linearGradient>
      <radialGradient id="paw-tone" cx="0.55" cy="0.6" r="0.6">
        <stop offset="0" stop-color="#c9c9cb"/>
        <stop offset="1" stop-color="#e6e6e7"/>
      </radialGradient>
    </defs>

    <rect class="pouch-body" x="332" y="133" width="515" height="832" rx="4" fill="var(--pouch-white)"/>

    <g clip-path="url(#pouch-clip)">
      <path class="top-band" d="M332 161 H560 Q578 161 590 176 Q602 161 620 161 H847"
            fill="none" stroke="var(--brand-green)" stroke-width="6"/>

      <rect class="paw-decor" x="353" y="254" width="163" height="186" rx="70" fill="url(#paw-tone)"
            role="img" aria-label="Large soft grey paw print decoration"/>

      <circle class="vet-badge" cx="450" cy="396" r="36" fill="#f4f4f4" stroke="#b7aa8c" stroke-width="3"/>

      <path class="feature-panel"
            d="M478 489 H847 V759 H478 Q366 759 366 624 Q366 489 478 489 Z"
            fill="var(--brand-green)"/>
      <circle class="photo-ring" cx="718" cy="484" r="158" fill="var(--brand-green)"/>
      <circle class="photo" cx="718" cy="484" r="146" fill="url(#photo-tone)"
              role="img" aria-label="Photo of the white wrinkled brand ambassador dog looking up at a butterfly"/>

      <rect class="bottom-band" x="332" y="906" width="515" height="30" fill="var(--brand-green)"/>
    </g>

    <circle class="brand-mark" cx="590" cy="222" r="16" fill="none" stroke="var(--brand-green)" stroke-width="2"/>

    <circle class="thc-badge" cx="600" cy="775" r="27" fill="none" stroke="var(--ink)" stroke-width="2" stroke-dasharray="2 5"/>
    <circle class="diet-badge" cx="410" cy="817" r="23" fill="none" stroke="var(--brand-green)" stroke-width="1.5"/>
    <circle class="diet-badge" cx="459" cy="822" r="23" fill="none" stroke="var(--brand-green)" stroke-width="1.5"/>

    <rect class="flavor-illustration" x="704" y="780" width="62" height="108" rx="24" fill="#d3e3dc" opacity="0.8"
          role="img" aria-label="Faint green chicken illustration"/>
  </svg>

  <div class="label brand-name">VERDANEL</div>
  <div class="label brand-sub">For Animals</div>

  <div class="label line-name">VerdaBites<sup>TM</sup></div>
  <div class="label product-cbd">CBD</div>
  <div class="label product-treats">TREATS</div>
  <div class="label dose">CBD 250mg</div>
  <div class="label benefits">SUPPORT | CALM | EASE</div>

  <div class="label thc-level">0,0%</div>
  <div class="label flavor"><span class="flavor-main">CHICKEN</span><span class="flavor-sub">Flavor</span></div>
  <div class="label net-weight">Net wt: 120g</div>
</div>
</body>
</html>
```